Law Offices business card

Hi there, I'll need business card for the Law Offices of Tobin Haskell. The information must convey his strategic approach and quick resolution to complex business litigation needs. Please emphasize Civil Litigation, Corporate Law, Business Governance and Real Estate Law. Tobin has over 25 years of experience in these fields.The card should be modern and edgy and the message should be clear. Please consult his current website for ideas.

Business

```html
<!DOCTYPE html>
<html lang="en">
<head>
<meta charset="utf-8">
<title>Law Offices of Tobin Haskell – Business Card</title>
<link rel="stylesheet" href="https://fonts.googleapis.com/css2?family=Source+Sans+3:wght@400;600;700&family=Cormorant+Garamond:wght@500;600&display=swap">
<style>
  :root {
    --backdrop: #e9e7e4;
    --card: #ffffff;
    --ink: #1a1a1a;
    --muted: #444444;
    --accent: #e8741e;
    --mark: #222222;
  }
  * { margin: 0; padding: 0; box-sizing: border-box; }
  html, body { width: 1200px; height: 900px; overflow: hidden; }
  body {
    position: relative;
    background: var(--backdrop);
    font-family: "Source Sans 3", "Myriad Pro", Arial, sans-serif;
    color: var(--ink);
  }
  .card {
    position: absolute;
    background: var(--card);
    box-shadow: 0 6px 20px rgba(0,0,0,0.12);
  }
  .card--front { left: 238px; top: 62px; width: 555px; height: 342px; }
  .card--back  { left: 458px; top: 519px; width: 559px; height: 342px; }

  .brand-dot {
    position: absolute;
    border-radius: 50%;
    border: 6px solid var(--mark);
  }
  .card--front .brand-dot { left: 74px; top: 81px; width: 180px; height: 180px; }
  .card--back  .brand-dot { left: 90px; top: 93px; width: 106px; height: 106px; border-width: 5px; }

  .contact-block { position: absolute; left: 302px; top: 73px; }
  .person-name { font-size: 21px; font-weight: 600; color: var(--accent); line-height: 1.1; }
  .person-role { font-size: 15px; line-height: 1.3; margin-bottom: 14px; }
  .address { font-size: 15px; line-height: 20px; margin-bottom: 13px; }
  .contact-list { list-style: none; font-size: 15px; }
  .contact-list li { display: flex; align-items: center; height: 23px; }
  .contact-list svg { width: 11px; height: 11px; margin: 0 12px 0 3px; fill: var(--accent); flex: none; }

  .firm-name {
    position: absolute; left: 240px; top: 114px;
    font-family: "Cormorant Garamond", "Trajan Pro", Georgia, serif;
    font-weight: 500; font-variant: small-caps;
    letter-spacing: 1.5px;
  }
  .firm-name span { display: block; }
  .firm-name .line-1 { font-size: 34px; line-height: 36px; color: var(--accent); }
  .firm-name .line-2 { font-size: 26px; line-height: 30px; color: var(--ink); font-weight: 600; }

  .practice-areas {
    position: absolute; left: 0; right: 0; top: 270px;
    text-align: center; font-size: 14.5px; font-weight: 700; line-height: 20px;
  }
  .experience {
    position: absolute; left: 0; right: 0; top: 294px;
    text-align: center; font-size: 13px; font-weight: 400; color: var(--muted);
    letter-spacing: 0.5px;
  }
</style>
</head>
<body>

<section class="card card--front" aria-label="Business card front">
  <div class="brand-dot" aria-hidden="true"></div>
  <div class="contact-block">
    <p class="person-name">Tobin Haskell</p>
    <p class="person-role">Attorney</p>
    <p class="address">318B Harbor Lane<br>Coral Point, Florida 33412</p>
    <ul class="contact-list">
      <li><svg viewBox="0 0 12 12"><path d="M2.5 0.5l2 2.3-1.2 1.5c.7 1.6 2 2.9 3.5 3.6l1.4-1.2 2.3 2-1.3 2.3C4.5 10.8 1.2 7.5.4 2z"/></svg>561-555-0142</li>
      <li><svg viewBox="0 0 12 12"><path d="M3 0h5l2 2v3h1.5v7H.5V5H2V0h1zm0 1v4h6V2.5L7.5 1zM2 7v1.5h2V7zm3 0v1.5h2V7zm3 0v1.5h2V7z"/></svg>561-555-0187</li>
      <li><svg viewBox="0 0 12 12"><path d="M0 2h12v1L6 7 0 3zm0 2.3l6 4 6-4V10H0z"/></svg>tobin@haskelllaw.com</li>
      <li><svg viewBox="0 0 12 12"><circle cx="6" cy="6" r="6"/><path d="M1 6h10M6 1c2 2 2 8 0 10M6 1c-2 2-2 8 0 10" stroke="#fff" stroke-width="1" fill="none"/></svg>www.haskelllaw.com</li>
    </ul>
  </div>
</section>

<section class="card card--back" aria-label="Business card back">
  <div class="brand-dot" aria-hidden="true"></div>
  <h1 class="firm-name">
    <span class="line-1">Law Offices</span>
    <span class="line-2">Of Tobin Haskell</span>
  </h1>
  <p class="practice-areas">Civil Litigation | Corporate Law | Business Governance | Real Estate Law</p>
  <p class="experience">Over 25 Years of Experience</p>
</section>

</body>
</html>
```